"VEX" Web Design Project

We need a create a webpage for a Streaming device product with sucription that we're going lo launch(like a lumo or pebble tv but comes with a possibily of monthly sucription of live tv channels).
The name of the product is "VEX" (vivid exchange viewing)

We are looking for something simple and with quality. Something webpages that we like are www.skyrune.com www.tindle.tv (our product will be very similar to tindle so you canuse for the menu an information reference, we're going to be more features because we are based on orbix so users can download all the apps from the marlow appmarket)
Also our remote control are gyroscopic (means like the zep remote) for many games.
We are working also in the logo so you can also see in our package and logo contest named: "HOME CAST UNIT: Box-unit-emblem" the Design #: 1768146 are the logo that maybe we're going to choose.

this is the link of our manufacturer to have on idea of the features of the device;
http://www.varnolux.com/pa/qbx730.asp

We like one color on the logo. But we want to see the logo in this colors: white,black ,light blue.

Thanks

Hi,
you can use for reference the TINDLE.TV webpage (look and feel, conten, information and & of pages..) also skyrune.tv as (look & feel).

Information to add:
In the case of the content the basic different is our device is orbix based. So only for reference of information to add (because we don't like lood and feel!!)  please use the info of  this links:

Spanish:
http://www.tolvaro.es/
products:
http://www.tolvaro.es/tolvaro-ZK830.html
http://www.tolvaro.es/descargas.html
http://www.tolvaro.es/about.html
http://www.tolvaro.es/contact.html
http://www.tolvaro.es/distribuidores.html

English:
http://www.tolvaro.com/product.asp?id=166
http://www.tolvaro.com/news.asp
http://www.tolvaro.com/support.asp
http://www.tolvaro.com/where-to-buy.asp
http://www.tolvaro.com/down.asp?id=1
http://www.tolvaro.com/about-us.asp

Note: are the same info but we're going to have only one model called: "VEX" . So we're going to by the devices to this manufacturer but we're going to rebranded...

AGAIN WE DON'T LIKE THE LOOK & FEEL OF THE LAST LINKS (ARE HORRIBLE) PLEASE USE AS A REFRENCE OF "LOOK & FEEL"  WWW.TINDLE.TV OR SKYRUNE.COM

https://www.filecrate-demo.net/sh/qx8831pwwr7mbel/R29KdTesoq

This files can help for the branding and pictures

Can you change the photos of the Slatex's per someone looking TV? One of the advantage of our product vrs conventional tv cable service is that we are Unplugged , we are Cord cutters. With our VEX device people can see TV on their home, their office, their vacation home. Because they can tke with them our device and conect to the internet and can see TV. 
Another advantage if for exmple our partnership with http://www.castorelay.tv/ so people can use their smartphones and tables as a remote control. But not normal remote control, totally interactive remote control and can share also all the network, my phone, and internet content to the TV by our VEX device. 

Please see the attached file. you can use something similar...

Target Market(s)

under 40 years. young people.

Industry/Entity Type

Tv

```html
<!DOCTYPE html>
<html lang="en">
<head>
<meta charset="utf-8">
<title>VEX — Media Streaming</title>
<link href="https://fonts.googleapis.com/css2?family=Arimo:wght@400;700&family=Montserrat:wght@600;700&family=Open+Sans:wght@400;600;700&family=Roboto+Condensed:wght@700&display=swap" rel="stylesheet">
<style>
  :root{
    --ink:#222222;
    --nav:#1f1f1f;
    --blue:#2f9bcb;
    --blue-bright:#3fb0e2;
    --link-blue:#2a8fc4;
    --grey-text:#7a7a7a;
    --white:#ffffff;
    --footer:#262626;
    --footer-text:#e4e4e4;
    --paper:#ffffff;
  }
  *{margin:0;padding:0;box-sizing:border-box}
  html,body{width:838px;height:1200px;overflow:hidden;background:var(--paper)}
  body{font-family:"Arimo",Arial,sans-serif;color:var(--ink)}
  .page{position:relative;width:838px;height:1200px;overflow:hidden}
  .abs{position:absolute}

  /* navigation */
  .topbar{left:0;top:0;width:838px;height:32px;background:var(--nav)}
  .brand{left:176px;top:5px;display:flex;align-items:center;gap:5px;
    font:700 19px/22px "Arimo",sans-serif;color:var(--blue-bright)}
  .brand-dot{width:15px;height:15px;border-radius:50%;background:var(--blue-bright)}
  .menu a{position:absolute;top:11px;font:400 8px/10px "Arimo",sans-serif;color:var(--white);text-decoration:none}

  /* hero */
  .hero{left:0;top:32px;width:838px;height:298px;
    background:linear-gradient(180deg,#b8b4ad 0%,#a89a88 35%,#6f7a86 70%,#3d4550 100%)}
  .hero-strip{left:0;top:318px;width:838px;height:12px;background:#2a2a2a}
  .tagline{left:0;top:71px;width:838px;text-align:center;
    font:400 13px/14px "Arimo",sans-serif;letter-spacing:6px;color:rgba(255,255,255,.85)}
  .headline{left:0;top:96px;width:838px;text-align:center;
    font:700 18px/22px "Arimo",sans-serif;color:var(--white);text-shadow:0 1px 3px rgba(0,0,0,.35)}
  .cta-start{left:360px;top:135px;width:133px;height:39px;border:3px solid #d8e6ee;border-radius:2px;
    background:linear-gradient(180deg,#6cc9f2,#2e9fd6);color:var(--white);
    font:400 12px/33px "Arimo",sans-serif;text-align:center}
  .device{left:322px;top:215px;width:207px;height:110px;border-radius:6px;
    background:linear-gradient(180deg,#3a3a3a,#0d0d0d)}

  /* welcome */
  .welcome-title{left:168px;top:373px;font:400 17px/20px "Arimo",sans-serif;color:var(--ink)}
  .welcome-copy{left:168px;top:413px;width:268px;font:400 12px/17px "Arimo",sans-serif;color:var(--grey-text)}
  .btn{height:20px;font:400 10px/20px "Arimo",sans-serif;color:var(--white);text-align:center}
  .btn-more{left:166px;top:507px;width:67px;background:var(--blue)}
  .btn-specs{left:241px;top:507px;width:66px;background:var(--ink)}
  .monitor{left:494px;top:374px;width:174px;height:134px;border-radius:3px;
    background:linear-gradient(180deg,#1a1a1a,#4a4a4a 55%,#cfcfcf 100%)}

  /* features */
  .features{left:0;top:552px;width:838px;height:203px;background:var(--blue)}
  .feature{position:absolute;top:26px;width:160px;text-align:center;color:var(--white)}
  .feature svg{display:block;margin:0 auto}
  .feature h3{margin-top:19px;font:700 12px/14px "Roboto Condensed",sans-serif}
  .feature p{margin-top:12px;font:400 6px/8px "Open Sans",sans-serif}
  .feature a{display:inline-block;margin-top:22px;font:400 6px/8px "Open Sans",sans-serif;color:var(--white);text-decoration:underline}

  /* lower info */
  .col-title{font:700 8px/10px "Open Sans",sans-serif;color:var(--ink)}
  .quick{left:169px;top:795px}
  .quick ul{list-style:none;margin-top:7px}
  .quick li{font:400 6.5px/10.8px "Open Sans",sans-serif;color:var(--ink)}
  .socials{display:flex;gap:3px;margin-top:6px}
  .socials span{width:9px;height:9px;border-radius:50%;background:var(--ink)}
  .testimonials{left:259px;top:795px}
  .portrait{left:258px;top:810px;width:79px;height:81px;background:linear-gradient(180deg,#e9e6e2,#c9c2ba)}
  .quote{left:348px;top:814px;width:118px;font:400 6.5px/9px "Open Sans",sans-serif;color:var(--ink)}
  .quote cite{display:block;margin-top:6px;font-style:normal;color:var(--link-blue)}
  .tweets{left:477px;top:795px}
  .tweet{position:absolute;left:477px;width:200px}
  .avatar{position:absolute;left:0;top:0;width:28px;height:28px;background:linear-gradient(180deg,#b9c4cc,#7b8790)}
  .tweet p{position:absolute;left:32px;top:0;width:160px;font:400 6px/8.5px "Open Sans",sans-serif;color:var(--ink)}
  .tweet b{font-weight:400;color:var(--link-blue)}

  /* call to action */
  .cta-band{left:0;top:974px;width:838px;height:56px;background:var(--blue)}
  .cta-text{left:175px;top:988px;font:600 18px/24px "Montserrat",sans-serif;color:var(--white)}
  .btn-buy{left:547px;top:988px;width:91px;height:25px;background:var(--white);
    font:600 11px/25px "Open Sans",sans-serif;color:#9aa3a8;text-align:center}

  /* footer */
  .footer{left:0;top:1030px;width:838px;height:170px;background:var(--footer)}
  .footer-col{position:absolute;top:1066px;list-style:none}
  .footer-col li{font:400 7px/8.4px "Arimo",sans-serif;color:var(--footer-text)}
</style>
</head>
<body>
<div class="page">

  <header>
    <div class="abs topbar"></div>
    <div class="abs brand"><span class="brand-dot"></span>VEX</div>
    <nav class="menu">
      <a style="left:450px">Home</a>
      <a style="left:497px">VEX</a>
      <a style="left:540px">About</a>
      <a style="left:588px">Services</a>
      <a style="left:640px">Contact</a>
    </nav>
  </header>

  <section>
    <div class="abs hero" role="img" aria-label="Blurred photo of young friends watching TV on a sofa"></div>
    <div class="abs hero-strip"></div>
    <p class="abs tagline">vivid exchange viewing</p>
    <h1 class="abs headline">VEX Media Streaming Redefining Your Experience</h1>
    <div class="abs cta-start">GET STARTED</div>
    <div class="abs device" role="img" aria-label="Photo of the black VEX streaming box"></div>
  </section>

  <section>
    <h2 class="abs welcome-title">Welcome to VEX</h2>
    <p class="abs welcome-copy">Lorem ipsum dolor sit amet, vim deleniti scrip-torem ut, sit an sanctus tibique cotidieque. Id cetero splendide cum, vel et fierent adversarium, ei putant repudiandae usu. Qui elit ignota in, ius diceret recusabo in, in usu convenire salutandi</p>
    <div class="abs btn btn-more">learn more</div>
    <div class="abs btn btn-specs">specs</div>
    <div class="abs monitor" role="img" aria-label="Photo of a desktop monitor showing people watching TV, with the VEX box in front"></div>
  </section>

  <section class="abs features">
    <div class="feature" style="left:141px">
      <svg width="28" height="28" viewBox="0 0 28 28" fill="none" stroke="#fff" stroke-width="2"><rect x="3" y="6" width="22" height="19" rx="1"/><path d="M3 10h22M7 6l3 4M13 6l3 4M19 6l3 4"/><path d="M11 13v9l7-4.5z" fill="#fff" stroke="none"/></svg>
      <h3>Plug &amp; Play</h3>
      <p>Can you change the photos of the Slatex's per someone looking TV? VEX of the advantage of our product vs conventional tv cable service is that we are Unplugged , we are Cord cutters.</p>
      <a>Keep reading</a>
    </div>
    <div class="feature" style="left:330px">
      <svg width="28" height="28" viewBox="0 0 28 28" fill="#fff"><rect x="10" y="3" width="8" height="7"/><rect x="3" y="18" width="8" height="7"/><rect x="17" y="18" width="8" height="7"/><path d="M13 10h2v4h6v4h-2v-2H9v2H7v-4h6z"/></svg>
      <h3>Easy Installing</h3>
      <p>Can you change the photos of the Slatex's per someone looking TV? VEX of the advantage of our product vs conventional tv cable service is that we are Unplugged , we are Cord cutters.</p>
      <a>Keep reading</a>
    </div>
    <div class="feature" style="left:521px">
      <svg width="28" height="28" viewBox="0 0 28 28" fill="none" stroke="#fff" stroke-width="2"><rect x="8" y="2" width="12" height="24" rx="2"/><path d="M8 6h12M8 21h12"/><circle cx="14" cy="23.5" r="1" fill="#fff"/></svg>
      <h3>Watch Everywhere</h3>
      <p>Can you change the photos of the Slatex's per someone looking TV? VEX of the advantage of our product vs conventional tv cable service is that we are Unplugged , we are Cord cutters.</p>
      <a>Keep reading</a>
    </div>
  </section>

  <section>
    <div class="abs quick">
      <h4 class="col-title">Quick Links</h4>
      <ul>
        <li>Home</li><li>Our Services</li><li>Latest Jobs (Samples)</li><li>About Us</li><li>Sign Up</li><li>Our Advantages</li><li>Featured Cases</li><li>Contact Us</li>
      </ul>
      <div class="socials"><span></span><span></span><span></span><span></span></div>
    </div>

    <h4 class="abs col-title testimonials">Customer Testimonials</h4>
    <div class="abs portrait" role="img" aria-label="Portrait photo of a customer"></div>
    <blockquote class="abs quote">"I have been working with Kelvo Media guys for a few months et quam diam, nec venenatis risus. Nunc ultricies massa quis lectus dictum id fermentum lacus rhoncus."
      <cite>Dane - Lumen Row Agency</cite>
    </blockquote>

    <h4 class="abs col-title tweets">From Twittsphere</h4>
    <div class="tweet" style="top:812px"><div class="avatar" role="img" aria-label="User avatar photo"></div><p><b>@quillmarsh1973</b> Nullam magna augue, sollicitudin sed auctor vitae, dignissim ultricies libero. Maecenas et augue quis tortor lacinia ultricies #KelvoMedia2013</p></div>
    <div class="tweet" style="top:846px"><div class="avatar" role="img" aria-label="User avatar photo"></div><p><b>@tarnfield</b> Nulla eu dolor eros, ut volutpat magna. Quisque faucibus sem ac lectus convallis rhoncus. #KelvoMedia2013</p></div>
    <div class="tweet" style="top:881px"><div class="avatar" role="img" aria-label="User avatar photo"></div><p><b>@quillmarsh1973</b> Praesent massa urna, dapibus fringilla euismod congue, dignissim ut est. Proin porttitor laoreet semper #KelvoMedia2013</p></div>
  </section>

  <section>
    <div class="abs cta-band"></div>
    <h2 class="abs cta-text">The ultimate streaming experience</h2>
    <div class="abs btn-buy">buy VEX</div>
  </section>

  <footer>
    <div class="abs footer"></div>
    <ul class="footer-col" style="left:189px"><li>About</li><li>Blog</li><li>Tindle Box</li><li>Jobs</li><li>Privacy</li><li>Terms of Use</li><li>DMCA</li><li>Returns</li><li>Buy</li><li>Circlepage</li><li>Chirpline</li></ul>
    <ul class="footer-col" style="left:328px"><li>About</li><li>Blog</li><li>Tindle Box</li><li>Jobs</li><li>Privacy</li><li>Terms of Use</li><li>DMCA</li><li>Returns</li><li>Buy</li><li>Circlepage</li><li>Chirpline</li></ul>
    <ul class="footer-col" style="left:465px"><li>About</li><li>Blog</li><li>Tindle Box</li><li>Jobs</li><li>Privacy</li><li>Terms of Use</li><li>DMCA</li><li>Returns</li><li>Buy</li><li>Circlepage</li><li>Chirpline</li></ul>
    <ul class="footer-col" style="left:604px"><li>About</li><li>Blog</li><li>Tindle Box</li><li>Jobs</li><li>Privacy</li><li>Terms of Use</li><li>DMCA</li><li>Returns</li><li>Buy</li><li>Circlepage</li><li>Chirpline</li></ul>
  </footer>

</div>
</body>
</html>
```